Financial Advisor Resource Firm needs business card design

Need business card design for company in Omaha NE called Tallowbrook Partners. We provide resources to financial advisors....workshop programs, retirement analysis, and insurance planning. I would like to see designs that use grays, greens, black, and white colors. The final design should communicate 'collaboration' and be simple yet attractive to financial planning clients. I will attached our logo and another picture of a puzzle piece coming together. I would like the incorporate the puzzle picture somehow, maybe on the back somehow, with color or just the gray scale....OR, the picture be the front of the card with 'Tallowbrook' definition on it (see upload) and then company logo, employee name, title, address on the back (see ppt uploaded). The following disclosure needs to be included somewhere- Advisory services offered through Marlowe Ridge Advisors, LLC.
Updates

I uploaded a svg and ai file of the logo

Target Market(s)

Financial planning clients and financial advisors....so pretty diverse age range of about 40-70.

Industry/Entity Type

Financial Planning

Contact Information for Business Card

Dennis K. Holloway, MBA
Founder/President
5727 E. Larkspur Avenue
Suite 418
Omaha, NE 68297
Phone- (402) 555-0147
Cell- (402) 555-0183
Fax- (402) 555-0129
email- dennis@tallowbrookgroup.example
web address- www.tallowbrookgroup.example

Colors
1b1b1b
474747
d3d3d3
ffffff
9bcb3c
abd036

Requirements
Must have
• Must include logo provided, must be 2 sided, and must have disclosure...all of these items listed in project description

```html
<!DOCTYPE html>
<html lang="en">
<head>
<meta charset="utf-8">
<title>Tallowbrook Partners — Business Card</title>
<link href="https://fonts.googleapis.com/css2?family=Work+Sans:wght@400;500;600&display=swap" rel="stylesheet">
<style>
  :root {
    --stage: #3b3430;
    --card: #1b1b1b;
    --card-edge: #262626;
    --green: #9bcb3c;
    --green-bright: #abd036;
    --white: #ffffff;
    --light-gray: #d3d3d3;
    --mid-gray: #474747;
    --muted: #8a8a8a;
  }
  * { box-sizing: border-box; margin: 0; padding: 0; }
  html, body {
    width: 1200px; height: 715px; overflow: hidden;
    background: var(--stage);
    font-family: "Work Sans", Arial, sans-serif;
  }
  .sheet {
    position: relative; width: 1200px; height: 715px;
    display: flex; align-items: center; justify-content: center; gap: 50px;
  }
  .card {
    position: relative; width: 520px; height: 297px;
    background: var(--card);
    border: 1px solid var(--card-edge);
    box-shadow: 0 10px 30px rgba(0,0,0,.45);
    overflow: hidden;
  }
  .wordmark {
    display: flex; align-items: center; gap: 10px;
    color: var(--white); font-weight: 600; letter-spacing: .04em;
    text-transform: uppercase; white-space: nowrap;
  }
  .wordmark__dot {
    width: 14px; height: 14px; border-radius: 50%; background: var(--green);
  }
  /* Front */
  .card--front { display: flex; align-items: center; justify-content: center; }
  .card--front .wordmark { font-size: 27px; }
  .disclosure {
    position: absolute; left: 0; right: 0; bottom: 22px;
    text-align: center; color: var(--muted);
    font-size: 10px; letter-spacing: .02em;
  }
  /* Back */
  .card--back .wordmark { position: absolute; left: 26px; top: 30px; font-size: 19px; }
  .divider {
    position: absolute; left: 30px; right: 62px; top: 140px;
    height: 1px; background: var(--green); opacity: .8;
  }
  .identity {
    position: absolute; right: 62px; top: 92px; text-align: right;
  }
  .identity__name { color: var(--green); font-size: 21px; font-weight: 500; }
  .identity__title { color: var(--white); font-size: 13px; margin-top: 3px; }
  .contact {
    position: absolute; left: 30px; top: 152px; list-style: none;
    color: var(--white); font-size: 11.5px; line-height: 18px;
  }
  .contact li { display: flex; align-items: center; gap: 8px; white-space: nowrap; }
  .contact svg { width: 9px; height: 9px; fill: var(--green); flex: none; }
  .contact .accent { color: var(--green); }
  .address {
    position: absolute; right: 62px; bottom: 36px; text-align: right;
    color: var(--white); font-size: 13px; line-height: 19px; font-style: normal;
  }
  .stripe { position: absolute; left: 0; right: 0; bottom: 0; height: 9px; display: flex; }
  .stripe__white { width: 42%; background: var(--white); }
  .stripe__green { flex: 1; background: var(--green-bright); }
</style>
</head>
<body>
<main class="sheet">
  <section class="card card--front" aria-label="Card front">
    <div class="wordmark"><span class="wordmark__dot"></span>Tallowbrook Partners</div>
    <p class="disclosure">Advisory services offered through Marlowe Ridge Advisors, LLC.</p>
  </section>

  <section class="card card--back" aria-label="Card back">
    <div class="wordmark"><span class="wordmark__dot"></span>Tallowbrook Partners</div>

    <div class="identity">
      <p class="identity__name">Dennis K. Holloway, MBA</p>
      <p class="identity__title">Founder/President</p>
    </div>
    <div class="divider"></div>

    <ul class="contact">
      <li><svg viewBox="0 0 10 10"><path d="M2 0h2l1 2.5-1.3 1A5 5 0 0 0 6.5 6.3l1-1.3L10 6v2c0 1-1 2-2 2C4 10 0 6 0 2 0 1 1 0 2 0z"/></svg><span>(402) 555-0147</span></li>
      <li><svg viewBox="0 0 10 10"><path d="M2.5 0h5v10h-5zM3.5 1v7h3V1z"/></svg><span>(402) 555-0183</span></li>
      <li><svg viewBox="0 0 10 10"><path d="M2 0h5v3H2zM0 3.5h10V8H8v2H2V8H0zM3 7v2h4V7z"/></svg><span>(402) 555-0129</span></li>
      <li><svg viewBox="0 0 10 10"><path d="M0 1.5h10v7H0zM1 2.5v.3L5 5.5l4-2.7v-.3z"/></svg><span>dennis@tallowbrookgroup.example</span></li>
      <li><svg viewBox="0 0 10 10"><path d="M5 0a5 5 0 1 0 0 10A5 5 0 0 0 5 0zm0 1.2a3.8 3.8 0 1 1 0 7.6 3.8 3.8 0 0 1 0-7.6zM1.5 4.5h7v1h-7z"/></svg><span>www.<span class="accent">tallowbrookgroup</span>.example</span></li>
    </ul>

    <address class="address">
      5727 E. Larkspur Avenue<br>
      Suite 418 Omaha, NE 68297
    </address>

    <div class="stripe"><span class="stripe__white"></span><span class="stripe__green"></span></div>
  </section>
</main>
</body>
</html>
```